Flyer/Poster to promote Bicycle Race

We need a flyer that promotes a bicycle race in downtown Denver. It need to inspire spectators to come watch and bicycle racers to come race. It benefits the Cedar Hollow Cycling Club is getting urban kids on bikes; sharing healthy lifestyle and values
. We want the colors to be the colors of the logo - blue & red. Community Partnerships must have their logos on the flyer. Flyer must be able to be printed in 8 1/2 x 11 and 11 x 17

Target Market(s)

Neighborhood residents, athletes, cyclists

Industry/Entity Type

Non Profit

Font styles to use
Serif
Sans Serif

Colors
0592cd
ec1f27

Requirements
Must have
• Sunday, July 31, 2016
• Schedule:
• • Racing starts at 7:00am
• • Fun Ride on the Race Course at 12pm
• • Expo & Festival 10am – 6pm
• A Bike Race for Amateurs and Professionals
• A Bike Race for the young, the old & everyone in the middle.
• Great for spectators. Hang out, watch the action & explore the Festival
• Grab a bite to eat & cheer on the racers as they fly around the corners
• Special activities for kids: Pelton Course, Barnaby the Goat & More!!
• Teodoro Vasquez WLMR Music Director and Afternoon by the Creekside host will be onsite!
• Start/Finish/Festival will be on Harlow St between 4th Ave & 6th Ave
• Net proceeds benefit the Cedar Hollow Cycling Club dedicated to getting urban youth on bikes; sharing healthy lifestyle and values
• Special thanks to the Pemberton Foundation for their ongoing support
• HARLOWLOOPRACE.COM

```html
<!DOCTYPE html>
<html lang="en">
<head>
<meta charset="utf-8">
<title>The Harlow St Crit – Poster</title>
<link rel="stylesheet" href="https://fonts.googleapis.com/css2?family=PT+Sans+Narrow:wght@400;700&display=swap">
<style>
  :root{
    --bg:#e6e6e6;
    --red:#ec1f27;
    --blue:#0592cd;
    --ink:#1e2530;
    --white:#ffffff;
    --photo-light:#bdbdbd;
    --photo-dark:#3a3a3a;
    --strip:#bdbdbd;
  }
  *{margin:0;padding:0;box-sizing:border-box}
  html,body{width:1161px;height:1200px;overflow:hidden;background:var(--bg)}
  body{font-family:"PT Sans Narrow","Arial Narrow",sans-serif}
  .poster{position:absolute;left:243px;top:69px;width:678px;height:1046px;background:var(--white);overflow:hidden;box-shadow:0 2px 6px rgba(0,0,0,.35)}
  .photo{position:absolute;left:0;top:0;width:678px;height:870px;
    background:linear-gradient(180deg,var(--photo-light) 0%,#8f8f8f 32%,#5f5f5f 62%,var(--photo-dark) 100%)}

  .date{position:absolute;left:43px;top:0;width:153px;height:297px;background:var(--red);color:var(--white);
    text-align:center;font-weight:700;line-height:1}
  .date .day{display:block;font-size:38px;margin-top:20px}
  .date .month{display:block;font-size:64px;margin-top:-2px}
  .date .num{display:block;font-size:128px;letter-spacing:-3px;margin-top:-6px}
  .date .year{display:block;font-size:44px;letter-spacing:6px;padding-left:6px;margin-top:-8px}

  .event-name{position:absolute;left:402px;top:109px;width:252px;height:94px;background:var(--white);
    border-radius:10px;color:var(--ink);font-weight:700;font-size:36px;line-height:38px;text-align:center;
    text-transform:uppercase;display:flex;align-items:center;justify-content:center}

  .schedule{position:absolute;left:0;top:350px;width:678px;text-align:center}
  .schedule h2{color:var(--white);font-size:68px;font-weight:700;line-height:72px}
  .slot{display:inline-block;font-weight:700;font-size:34px;line-height:37px;padding:0 18px;transform:skewX(-4deg)}
  .slot span{display:inline-block;transform:skewX(4deg)}
  .slot.red{background:var(--red);color:var(--white)}
  .slot.white{background:var(--white);color:#111}
  .slot.blue{background:var(--blue);color:var(--white)}

  .details{position:absolute;left:40px;top:559px;width:620px;display:grid;
    grid-template-columns:200px 206px 190px;grid-template-rows:88px 86px auto;column-gap:12px}
  .details p{position:relative;padding-left:18px;color:var(--white);font-weight:700;font-size:15px;line-height:19px}
  .details svg{position:absolute;left:0;top:4px}

  .partners{position:absolute;left:0;top:870px;width:678px;height:94px;background:var(--white);
    display:flex;align-items:center;justify-content:space-between;padding:0 10px}
  .partner{font-weight:700;font-size:12px;color:var(--ink);text-align:center;line-height:1.1}
  .badge{width:24px;height:24px;background:#3a3a3a}
  .badge.round{border-radius:50%;width:32px;height:32px;background:var(--red)}

  .footer{position:absolute;left:0;top:964px;width:678px;height:82px;background:var(--strip);
    display:flex;align-items:center;justify-content:center;color:var(--ink);font-weight:700;font-size:42px}
</style>
</head>
<body>
<main class="poster">
  <div class="photo" role="img" aria-label="Black and white photo of a pack of cyclists racing toward the camera past a finish-line banner"></div>

  <div class="date">
    <span class="day">SUNDAY</span>
    <span class="month">JULY</span>
    <span class="num">31</span>
    <span class="year">2016</span>
  </div>

  <div class="event-name">The Harlow St<br>Crit</div>

  <section class="schedule">
    <h2>SCHEDULE:</h2>
    <div><span class="slot red"><span>• RACING STARTS AT 7:00AM</span></span></div>
    <div><span class="slot white"><span>• FUN RIDE ON THE RACE COURSE AT 12PM</span></span></div>
    <div><span class="slot blue"><span>• EXPO &amp; FESTIVAL 10AM – 6PM</span></span></div>
  </section>

  <section class="details">
    <p><svg width="9" height="11" viewBox="0 0 10 12"><path d="M1 0l8 6-8 6 2-6z" fill="#ec1f27"/></svg>A Bike Race for Amateurs and Professionals</p>
    <p><svg width="9" height="11" viewBox="0 0 10 12"><path d="M1 0l8 6-8 6 2-6z" fill="#ec1f27"/></svg>A Bike Race for the young, the old &amp; every-one in the middle.</p>
    <p><svg width="9" height="11" viewBox="0 0 10 12"><path d="M1 0l8 6-8 6 2-6z" fill="#ec1f27"/></svg>Great for spectators. Hang out, watch the action &amp; explore the Festival</p>
    <p><svg width="9" height="11" viewBox="0 0 10 12"><path d="M1 0l8 6-8 6 2-6z" fill="#ec1f27"/></svg>Grab a bite to eat &amp; cheer on the racers as they fly around the corners</p>
    <p><svg width="9" height="11" viewBox="0 0 10 12"><path d="M1 0l8 6-8 6 2-6z" fill="#ec1f27"/></svg>Special activities for kids: Pelton Course, Barnaby the Goat &amp; More!!</p>
    <p><svg width="9" height="11" viewBox="0 0 10 12"><path d="M1 0l8 6-8 6 2-6z" fill="#ec1f27"/></svg>Teodoro Vasquez WLMR Music Director and Afternoon by the Creekside host will be onsite!</p>
    <p><svg width="9" height="11" viewBox="0 0 10 12"><path d="M1 0l8 6-8 6 2-6z" fill="#ec1f27"/></svg>Start/Finish/Festival will be on Harlow St between 4th Ave &amp; 6th Ave</p>
    <p><svg width="9" height="11" viewBox="0 0 10 12"><path d="M1 0l8 6-8 6 2-6z" fill="#ec1f27"/></svg>Net proceeds benefit the Cedar Hollow Cycling Club dedicated to getting urban youth on bikes; sharing healthy lifestyle and values</p>
    <p><svg width="9" height="11" viewBox="0 0 10 12"><path d="M1 0l8 6-8 6 2-6z" fill="#ec1f27"/></svg>Special thanks to the Pemberton Foundation for their ongoing support</p>
  </section>

  <section class="partners" aria-label="Community partners">
    <span class="partner">Cedar Hollow<br>Cycling Club</span>
    <span class="partner">WLMR</span>
    <span class="partner">Summit Valley TV</span>
    <span class="badge"></span>
    <span class="partner">Velo Sisters</span>
    <span class="badge round"></span>
    <span class="partner">Ridgeline</span>
    <span class="partner">Apex Seven</span>
    <span class="partner">Gilded Square</span>
    <span class="badge"></span>
    <span class="partner">Norvik</span>
  </section>

  <footer class="footer">HARLOWLOOPRACE.COM</footer>
</main>
</body>
</html>
```